Wedding Decor and Entertianment business card

Company - We run a weddings and events company called Amber Finch, we provide most entertainment and decor services to our customers.

Initial idea is ....
A simple business card with logo on the front, this will be spot varnish. On a matt black background.
The reverse will be simple contact information.

But happy to try things outside of the box and would welcome some crazy ideas.

Target Market(s)

wedding couples - 21 - 40
High end wedding venues.

Industry/Entity Type

Wedding

Contact Information for Business Card

01492 718 263
amberfinchevents.co.uk
rowan@amberfinchevents.co.uk
or
helena@amberfinchevents.co.uk

Requirements
Nice to have
• black matt background with spot varnish logo on the front.

```html
<!DOCTYPE html>
<html lang="en">
<head>
<meta charset="utf-8">
<title>Amber Finch – Business Card</title>
<link rel="stylesheet" href="https://fonts.googleapis.com/css2?family=Jost:wght@400&family=Montserrat:wght@400;500&display=swap">
<style>
  :root {
    --backdrop: #8fd0c4;
    --card-black: #000000;
    --card-white: #ffffff;
    --ink-navy: #2c3193;
    --tint-lavender: #c9cfe8;
    --tint-sky: #c6e6f1;
    --logo-white: #ffffff;
  }
  html, body {
    margin: 0;
    padding: 0;
    width: 1200px;
    height: 1200px;
    overflow: hidden;
    background: var(--backdrop);
  }
  .canvas {
    position: relative;
    width: 1200px;
    height: 1200px;
  }
  .card {
    position: absolute;
    left: 160px;
    width: 880px;
    height: 500px;
    box-shadow: 0 14px 30px rgba(0, 60, 50, 0.22);
    overflow: hidden;
  }
  .card--front {
    top: 70px;
    background: var(--card-black);
    display: flex;
    align-items: center;
    justify-content: center;
    gap: 30px;
  }
  .brand-mark {
    width: 64px;
    height: 64px;
    border: 3px solid var(--logo-white);
    border-radius: 50%;
    box-sizing: border-box;
  }
  .brand-name {
    font-family: "Jost", sans-serif;
    font-weight: 400;
    font-size: 46px;
    letter-spacing: 0.42em;
    color: var(--logo-white);
    margin-right: -0.42em;
  }
  .card--back {
    top: 630px;
    background: var(--card-white);
  }
  .back-shapes {
    position: absolute;
    inset: 0;
  }
  .phone {
    position: absolute;
    left: 66px;
    top: 62px;
    display: flex;
    align-items: center;
    gap: 22px;
    font-family: "Montserrat", sans-serif;
    font-weight: 400;
    font-size: 44px;
    color: var(--ink-navy);
  }
  .phone-icon {
    width: 34px;
    height: 34px;
  }
  .contact-lines {
    position: absolute;
    right: 58px;
    bottom: 62px;
    text-align: right;
    font-family: "Montserrat", sans-serif;
    font-weight: 400;
    font-size: 32px;
    line-height: 1.2;
    color: var(--ink-navy);
  }
  .contact-lines p { margin: 0; }
</style>
</head>
<body>
<main class="canvas">
  <section class="card card--front" aria-label="Card front">
    <span class="brand-mark" aria-hidden="true"></span>
    <span class="brand-name">AMBER FINCH</span>
  </section>

  <section class="card card--back" aria-label="Card back">
    <svg class="back-shapes" viewBox="0 0 880 500" preserveAspectRatio="none" aria-hidden="true">
      <polygon points="0,478 880,6 880,42" fill="var(--tint-sky)"/>
      <polygon points="0,478 880,42 880,500 0,500" fill="var(--tint-lavender)"/>
    </svg>
    <div class="phone">
      <svg class="phone-icon" viewBox="0 0 24 24" aria-hidden="true">
        <path fill="var(--ink-navy)" d="M6.6 2.2c.5-.3 1.1-.2 1.4.3l2.2 3.5c.3.5.2 1.1-.2 1.4L8.4 8.6c.9 2.6 3.5 5.6 6.2 6.9l1.3-1.6c.4-.4 1-.5 1.4-.2l3.5 2.1c.5.3.6.9.3 1.4l-1.4 2.4c-.4.7-1.2 1.1-2 .9C10.2 19.1 4.8 13.2 3.7 5.6c-.1-.8.3-1.5 1-1.9z"/>
      </svg>
      <span class="phone-number">01492 718 263</span>
    </div>
    <div class="contact-lines">
      <p class="website">amberfinchevents.co.uk</p>
      <p class="email">helena@amberfinchevents.co.uk</p>
    </div>
  </section>
</main>
</body>
</html>
```